Label Design Project for my tea product Imported from Japan

I have a tea importing business. I want someone to help me design a label for my Uji matcha tea product. I want the label to be modern, neat, and beautifully designed. I prefer it to be easily adaptable to other tea products that I will be importing.
Product name: Organic Uji Matcha
Company name: Calm Harbor Leaf Merchants
Description: Powdered Green Tea Matcha
Ceremonial grade premium quality
Directly imported from Japan
This product is going to be sold in the U.S. market, so please make sure that the label is in compliance with the FDA regulations.

Target Market(s)

High end tea consumers

Industry/Entity Type

Business

Requirements
Must have
• Marking of origin : product of Japan
• Imported by: Calm Harbor Leaf Merchants
• Leave space for Net weight, the name and place of business of the manufacturer.
• Ingredients: Green Tea 100%
• Nutrition list is not necessary.

```html
<!DOCTYPE html>
<html lang="en">
<head>
<meta charset="utf-8">
<title>Organic Uji Matcha Label</title>
<link rel="stylesheet" href="https://fonts.googleapis.com/css2?family=Lato:wght@700;900&family=Questrial&display=swap">
<style>
  :root {
    --backdrop: #9d9ea2;
    --paper: #e4e4e9;
    --panel: #a6c7b5;
    --ink: #2f9c62;
    --band: #c5d8cf;
  }
  * { box-sizing: border-box; margin: 0; padding: 0; }
  html, body {
    width: 1200px;
    height: 800px;
    overflow: hidden;
    background: var(--backdrop);
  }
  .label {
    position: absolute;
    left: 411px;
    top: 84px;
    width: 380px;
    height: 632px;
    background: var(--paper);
  }
  .label__band {
    position: absolute;
    left: 0;
    width: 100%;
    height: 22px;
    background: linear-gradient(180deg, var(--band), #b7cfc3);
  }
  .label__band--top { top: 0; }
  .label__band--bottom { bottom: 0; }
  .label__panel {
    position: absolute;
    left: 36px;
    top: 42px;
    width: 308px;
    height: 551px;
    border-radius: 20px;
    background: var(--panel);
    color: var(--ink);
    font-family: "Questrial", "Century Gothic", sans-serif;
    text-align: center;
  }
  .brand-box {
    position: absolute;
    left: 64px;
    top: 16px;
    width: 180px;
    height: 77px;
    border: 1.5px dashed var(--ink);
  }
  .brand-box__mark {
    display: flex;
    justify-content: center;
    align-items: center;
    gap: 5px;
    margin-top: 20px;
    font-size: 10px;
    letter-spacing: 0.5px;
  }
  .brand-box__dot {
    width: 9px;
    height: 9px;
    border-radius: 50%;
    background: var(--ink);
  }
  .brand-box__name {
    margin-top: 11px;
    font-family: "Lato", sans-serif;
    font-weight: 900;
    font-size: 9.5px;
    letter-spacing: 0.6px;
    text-transform: uppercase;
  }
  .product-name {
    position: absolute;
    left: 0;
    top: 120px;
    width: 100%;
    font-family: "Lato", sans-serif;
    font-weight: 700;
    font-size: 29px;
    letter-spacing: 0.2px;
  }
  .facts {
    position: absolute;
    left: 0;
    top: 216px;
    width: 100%;
  }
  .facts__label {
    display: inline-block;
    font-size: 10.5px;
    padding-bottom: 2px;
    border-bottom: 1px solid var(--ink);
  }
  .facts__value {
    font-size: 13.5px;
    margin: 5px 0 4px;
  }
  .facts__value--origin { font-size: 14px; }
  .cert-badge {
    position: absolute;
    left: 15px;
    top: 506px;
    width: 52px;
    height: 22px;
    border-radius: 3px;
    background: var(--ink);
  }
  .importer {
    position: absolute;
    right: 12px;
    top: 486px;
    width: 90px;
  }
  .importer__label { font-size: 6.5px; }
  .importer__mark {
    display: flex;
    justify-content: center;
    align-items: center;
    gap: 3px;
    margin-top: 6px;
    font-size: 5.5px;
  }
  .importer__dot {
    width: 5px;
    height: 5px;
    border-radius: 50%;
    background: var(--ink);
  }
  .importer__name {
    margin-top: 5px;
    font-family: "Lato", sans-serif;
    font-weight: 900;
    font-size: 5px;
    letter-spacing: 0.3px;
    text-transform: uppercase;
    white-space: nowrap;
  }
</style>
</head>
<body>
  <div class="label">
    <div class="label__band label__band--top" role="img" aria-label="Chevron pattern band"></div>

    <section class="label__panel">
      <div class="brand-box">
        <div class="brand-box__mark"><span class="brand-box__dot"></span>Calm Harbor</div>
        <div class="brand-box__name">Calm Harbor Leaf Merchants</div>
      </div>

      <h1 class="product-name">Organic Uji Matcha</h1>

      <div class="facts">
        <div class="facts__label">Ingredients :</div>
        <p class="facts__value">Green Tea 100%</p>
        <div class="facts__label">Marking of origin :</div>
        <p class="facts__value facts__value--origin">Product of Japan</p>
      </div>

      <div class="cert-badge" role="img" aria-label="Regulatory compliance badge"></div>

      <div class="importer">
        <div class="importer__label">Imported by :</div>
        <div class="importer__mark"><span class="importer__dot"></span>Calm Harbor</div>
        <div class="importer__name">Calm Harbor Leaf Merchants</div>
      </div>
    </section>

    <div class="label__band label__band--bottom" role="img" aria-label="Chevron pattern band"></div>
  </div>
</body>
</html>
```